Product Designer Business Card

Small product design, engineering and prototyping firm in need of a clean, professional business card design. To support our 3D design and drawing services, we offer 3D printing, molding, and casting of plastics, silicones, resins, etc. Our logo can still be modified/changed if necessary. The red/orange color is preferred, but may be substituted with blue or green, potentially. Either way, the colour of the logo should be match/compliment colors used throughout the design. One thought is to have the logo/contact info on one side, with the other side describing services offered, like with a small icon of 3D printer, molding, casting, and computer with a 3D model on-screen.
Industry/Entity Type
Mechanical Engineering
Contact Information for Business Card
Company: Halvick Design
Phone: 613-582-4179
Email: myles@halvickdesign.ca

```html
<!DOCTYPE html>
<html lang="en">
<head>
<meta charset="utf-8">
<title>Halvick Design — Business Card</title>
<link rel="stylesheet" href="https://fonts.googleapis.com/css2?family=Roboto:wght@400;500;700&display=swap">
<style>
  :root {
    --backdrop: #e6e6e6;
    --card: #2c2c2c;
    --edge: #e0262a;
    --red: #e0262a;
    --white: #f4f4f4;
    --rule: #6a6a6a;
  }
  * { margin: 0; padding: 0; box-sizing: border-box; }
  html, body { width: 1200px; height: 801px; overflow: hidden; }
  body {
    background: var(--backdrop);
    font-family: "Roboto", sans-serif;
    display: flex;
    align-items: center;
    justify-content: center;
    gap: 40px;
  }
  .card {
    width: 560px;
    height: 320px;
    background: var(--card);
    border: 3px solid var(--edge);
    position: relative;
    color: var(--white);
  }
  /* front */
  .card-front { display: flex; align-items: center; }
  .brand-block {
    width: 260px;
    display: flex;
    align-items: center;
    justify-content: center;
    gap: 12px;
  }
  .brand-dot { width: 26px; height: 26px; border-radius: 50%; background: var(--red); }
  .brand-name { font-size: 28px; font-weight: 500; color: var(--red); }
  .divider { width: 1px; height: 150px; background: var(--rule); }
  .contact-block { padding-left: 34px; }
  .person-name { font-size: 24px; font-weight: 700; color: var(--red); }
  .person-role { font-size: 17px; margin-bottom: 18px; }
  .contact-list { list-style: none; font-size: 15px; line-height: 1.75; }
  .contact-list li { display: flex; align-items: center; gap: 10px; }
  .contact-list svg { width: 13px; height: 13px; flex: none; }
  .web-accent { color: var(--red); }
  /* back */
  .card-back {
    display: flex;
    flex-direction: column;
    align-items: center;
    justify-content: center;
  }
  .back-brand { display: flex; align-items: center; gap: 16px; margin-bottom: 34px; }
  .back-brand .brand-dot { width: 44px; height: 44px; background: var(--white); }
  .back-brand .brand-name { font-size: 56px; color: var(--white); letter-spacing: 4px; font-weight: 400; }
  .services-title { font-size: 20px; font-weight: 500; color: var(--red); margin-bottom: 8px; letter-spacing: .5px; }
  .services-list { list-style: none; display: flex; font-size: 17px; }
  .services-list li + li::before {
    content: "";
    display: inline-block;
    width: 9px; height: 9px;
    border-radius: 50%;
    background: var(--red);
    margin: 0 9px 2px;
  }
</style>
</head>
<body>
  <section class="card card-front">
    <div class="brand-block">
      <span class="brand-dot"></span>
      <span class="brand-name">Halvick Design</span>
    </div>
    <div class="divider"></div>
    <div class="contact-block">
      <div class="person-name">Corin Vaskell</div>
      <div class="person-role">Manager</div>
      <ul class="contact-list">
        <li>
          <svg viewBox="0 0 16 16"><path d="M3 1l3 3-2 2c1 2 3 4 6 6l2-2 3 3-2 2C7 15 1 9 1 3z" fill="#e0262a"/></svg>
          613-582-4179
        </li>
        <li>
          <svg viewBox="0 0 16 16"><rect x="1" y="3" width="14" height="10" fill="none" stroke="#e0262a" stroke-width="1.6"/><path d="M1 3l7 6 7-6" fill="none" stroke="#e0262a" stroke-width="1.6"/></svg>
          myles@halvickdesign.ca
        </li>
        <li>
          <svg viewBox="0 0 16 16"><circle cx="8" cy="8" r="7" fill="#e0262a"/><path d="M1 8h14M8 1v14" stroke="#2c2c2c" stroke-width="1.2"/></svg>
          <span>www.<span class="web-accent">halvickdesign</span>.ca</span>
        </li>
      </ul>
    </div>
  </section>

  <section class="card card-back">
    <div class="back-brand">
      <span class="brand-dot"></span>
      <span class="brand-name">Halvick</span>
    </div>
    <div class="services-title">SERVICES OFFERED</div>
    <ul class="services-list">
      <li>3D Printer</li>
      <li>Molding</li>
      <li>Casting</li>
      <li>Computer</li>
    </ul>
  </section>
</body>
</html>
```